Upscale business cards needed for Board of Directors

We need professional business cards created for members of our family business Board of Directors. We would like these relatively simple and straightforward, but also with a unique element to set them apart. Probably stick with neutral and simple colors - white, grey etc. We need space for the traditional elements, including name, title, address, email/phone number. And we will be creating several from this template so it needs to be template that is easy to switch information in and out of.
Business
See description

```html
<!DOCTYPE html>
<html lang="en">
<head>
<meta charset="UTF-8">
<title>Harbormont Holdings – Business Card</title>
<link href="https://fonts.googleapis.com/css2?family=Exo+2:wght@400;600&display=swap" rel="stylesheet">
<style>
  :root {
    --panel-grey: #b2b2b2;
    --panel-grey-light: #bdbdbd;
    --card-white: #fbfbfb;
    --accent-gold: #aaa07a;
    --ink-dark: #2c2c2c;
    --ink-text: #333333;
  }
  html, body {
    margin: 0;
    padding: 0;
    width: 1200px;
    height: 686px;
    overflow: hidden;
    background: var(--card-white);
  }
  .card {
    position: relative;
    width: 1200px;
    height: 686px;
    background: var(--card-white);
    font-family: "Exo 2", sans-serif;
    color: var(--ink-text);
    overflow: hidden;
  }
  .brand-panel {
    position: absolute;
    left: 0;
    top: 0;
    width: 597px;
    height: 686px;
    background: linear-gradient(160deg, var(--panel-grey-light) 0%, var(--panel-grey) 60%, #adadad 100%);
    display: flex;
    align-items: center;
    justify-content: center;
  }
  .brand-name {
    margin: 0;
    font-size: 46px;
    font-weight: 600;
    color: var(--ink-dark);
    line-height: 1;
    white-space: nowrap;
  }
  .rule {
    position: absolute;
    height: 7px;
    background: var(--accent-gold);
  }
  .rule-top { left: 639px; top: 35px; width: 532px; }
  .rule-bottom { left: 646px; top: 643px; width: 532px; }
  .person {
    position: absolute;
    right: 74px;
    top: 262px;
    text-align: right;
  }
  .person-name {
    margin: 0;
    font-size: 56px;
    font-weight: 600;
    color: var(--ink-dark);
    line-height: 1;
  }
  .person-title {
    margin: 20px 0 0;
    font-size: 38px;
    font-weight: 400;
    line-height: 1;
  }
  .contact {
    position: absolute;
    right: 31px;
    top: 452px;
    text-align: right;
    font-size: 27px;
    line-height: 38px;
  }
  .contact p { margin: 0; }
  .contact .address { margin-bottom: 18px; }
</style>
</head>
<body>
  <div class="card">
    <div class="brand-panel">
      <p class="brand-name">Harbormont Holdings</p>
    </div>

    <div class="rule rule-top"></div>

    <div class="person">
      <h1 class="person-name">Daniel Reeve</h1>
      <p class="person-title">director</p>
    </div>

    <div class="contact">
      <p class="address">Address: Lorem ipsum dolor sit amet<br>consectetur adipiscing elit</p>
      <p class="phone">Phone:5550142837</p>
      <p class="email">E-mail:daniel.reeve@mailbox.com</p>
    </div>

    <div class="rule rule-bottom"></div>
  </div>
</body>
</html>
```